New Book Cover Design Project

Book Cover with this title and sub title
Where Auntie Found Her Quiet Orchard
The little book to be smart with your money and help the environment.
Walter P. Drune Ph. D.
Edith P. Drune
Picture below would be on the entire front cover. Words somehow incorporated for easy reading.

```html
<!DOCTYPE html>
<html lang="en">
<head>
<meta charset="utf-8">
<title>Where Auntie Found Her Quiet Orchard — Cover Wrap</title>
<link rel="stylesheet" href="https://fonts.googleapis.com/css2?family=Bebas+Neue&family=Montserrat:wght@600;700&family=Hind:wght@400;500&display=swap">
<style>
  :root {
    --backdrop: #ececec;
    --cover-yellow: #ebe21c;
    --navy: #1f3450;
    --slate: #3e4a62;
    --title-white: #ffffff;
    --sub-yellow: #f3ec3a;
    --sub-band: rgba(150, 150, 20, 0.6);
    --body-ink: #3a3a2a;
    --portrait-grey: #8a8a8a;
  }
  * { box-sizing: border-box; margin: 0; padding: 0; }
  html, body { width: 1200px; height: 924px; overflow: hidden; }
  body { background: var(--backdrop); font-family: "Hind", sans-serif; }
  .wrap {
    position: absolute; left: 150px; top: 82px;
    width: 900px; height: 760px;
    display: flex;
    box-shadow: 0 14px 40px rgba(0,0,0,0.18);
  }
  /* back cover */
  .back {
    position: relative; width: 425px; height: 100%;
    background: var(--cover-yellow);
    padding: 40px 30px 0;
  }
  .back-title {
    font-family: "Bebas Neue", sans-serif;
    color: var(--slate);
    font-size: 48px; line-height: 0.92;
    text-align: center;
    margin-bottom: 22px;
  }
  .back-blurb {
    font-size: 10.5px; line-height: 1.45; color: var(--body-ink);
    text-align: justify; margin-bottom: 22px;
  }
  .author-bio { display: flex; gap: 12px; margin-bottom: 16px; }
  .portrait { flex: 0 0 112px; height: 140px; background: linear-gradient(90deg, #666 0%, var(--portrait-grey) 50%); }
  .bio-name {
    font-family: "Montserrat", sans-serif; font-weight: 700;
    color: var(--slate); font-size: 15px; margin-bottom: 4px;
  }
  .bio-text { font-size: 10.5px; line-height: 1.35; color: var(--body-ink); text-align: justify; }
  .band {
    position: absolute; left: 0; right: 0; bottom: 0; height: 68px;
    background: var(--navy);
  }
  /* spine */
  .spine {
    position: relative; width: 50px; height: 100%;
    background: var(--cover-yellow);
    border-left: 1px solid rgba(0,0,0,0.08);
    border-right: 1px solid rgba(0,0,0,0.08);
  }
  .spine-text {
    position: absolute; left: 50%; top: 346px;
    transform: translate(-50%, -50%) rotate(-90deg);
    white-space: nowrap;
    font-family: "Montserrat", sans-serif; font-weight: 700;
    font-size: 11px; letter-spacing: 0.06em; color: var(--slate);
    display: flex; gap: 40px;
  }
  /* front cover */
  .front { position: relative; width: 425px; height: 100%; overflow: hidden; }
  .cover-photo {
    position: absolute; inset: 0;
    background:
      radial-gradient(ellipse 70% 45% at 50% 70%, #f2c81a 0%, #efd21e 45%, transparent 80%),
      linear-gradient(180deg, #5c6a48 0%, #7a6e58 22%, #8a7a4a 34%, #d9c21e 48%, #f0d220 70%, #e9cb1a 100%);
  }
  .front-title {
    position: relative;
    font-family: "Bebas Neue", sans-serif;
    color: var(--title-white);
    font-size: 64px; line-height: 0.94;
    text-align: center;
    padding-top: 44px;
    text-shadow: 0 2px 6px rgba(0,0,0,0.35);
  }
  .subtitle {
    position: absolute; left: 60px; right: 30px; top: 268px;
    background: var(--sub-band);
    color: var(--sub-yellow);
    font-size: 17px; line-height: 1.3; font-weight: 500;
    text-align: center; padding: 8px 10px;
  }
  .front .band {
    height: 96px;
    display: flex; flex-direction: column; justify-content: center; align-items: center;
    font-family: "Montserrat", sans-serif; font-weight: 700;
    color: var(--title-white); font-size: 20px; line-height: 1.1;
    text-transform: uppercase;
  }
</style>
</head>
<body>
  <div class="wrap">
    <section class="back">
      <h2 class="back-title">Where Auntie<br>Found Her Quiet<br>Orchard</h2>
      <p class="back-blurb">Lorem ipsum dolor sit amet, consectetuer adipiscing elit, sed diam nonummy nibh euismod tincidunt ut laoreet dolore magna aliquam erat volutpat. Ut wisi enim ad minim veniam, quis nostrud exerci tation ullamcorper suscipit lobortis nisl ut aliquip ex ea commodo consequat. Duis autem vel eum iriure dolor in hendrerit in vulputate velit esse molestie consequat, vel illum. Duis autem vel eum iriure dolor in hendrerit in vulputate velit esse molestie consequat, vel illum.</p>
      <div class="author-bio">
        <div class="portrait" role="img" aria-label="Author portrait of Walter P. Drune"></div>
        <div>
          <h3 class="bio-name">WALTER P. DRUNE PH. D.</h3>
          <p class="bio-text">Lorem ipsum dolor sit amet, consectetuer adipiscing elit, sed diam nonummy nibh euismod tincidunt ut laoreet dolore magna aliquam erat volutpat. Ut wisi enim ad minim veniam, quis nostrud exerci tation ullamcorper suscipit lobortis nisl.</p>
        </div>
      </div>
      <div class="author-bio">
        <div class="portrait" role="img" aria-label="Author portrait of Edith P. Drune"></div>
        <div>
          <h3 class="bio-name">EDITH P. DRUNE</h3>
          <p class="bio-text">Lorem ipsum dolor sit amet, consectetuer adipiscing elit, sed diam nonummy nibh euismod tincidunt ut laoreet dolore magna aliquam erat volutpat. Ut wisi enim ad minim veniam, quis nostrud exerci tation ullamcorper suscipit lobortis nisl.</p>
        </div>
      </div>
      <div class="band"></div>
    </section>

    <section class="spine">
      <div class="spine-text"><span>WHERE AUNTIE FOUND HER QUIET ORCHARD</span><span>WALTER P. DRUNE PH. D. | EDITH P. DRUNE</span></div>
      <div class="band"></div>
    </section>

    <section class="front">
      <div class="cover-photo" role="img" aria-label="Close-up photograph of a honeybee on a bright yellow dandelion, with green foliage behind"></div>
      <h1 class="front-title">Where Auntie<br>Found Her Quiet<br>Orchard</h1>
      <p class="subtitle">The little book to be smart with your<br>money and help the environment</p>
      <div class="band">
        <span>Walter P. Drune Ph. D.</span>
        <span>Edith P. Drune</span>
      </div>
    </section>
  </div>
</body>
</html>
```